Business Card Design

I'm a young beekeeper (22 years old) just starting out. I own and run 80 hives and would like to eventually build up to 1000. My aim is to run it in tandem with our family farm that is currently running sheep and beef. Unlike a number of honey companies on the East Coast (or the North Island, NZ) I am local and will expand onto the lease blocks that our family is also leasing. I want a simple plain logo/photo. The designer may wish to use one of the photos as a background outline or however they chose. The mountain is Aorangi and our farm borders one side of it.

Target Market(s)

From local land owners to wholesale honey buyers

Industry/Entity Type

Farm

Contact Information for Business Card

Pekeriu Honey
Manager Owner Manaia Brooks
email pekeriuhoney@tuimailbox.co.nz
mobile 0217394461

Requirements
Must have
• The details submitted. The brand Pekeriu Honey to be the main feature. The other details can be smaller.
Should not have
• Must not include a picture of a bee or hive. Use a modern font. Don't use koru but may incorporate poutama.

```html
<!DOCTYPE html>
<html lang="en">
<head>
<meta charset="utf-8">
<title>Pekeriu Honey – Business Card</title>
<link rel="stylesheet" href="https://fonts.googleapis.com/css2?family=Dancing+Script:wght@700&family=Quicksand:wght@300;400&display=swap">
<style>
  :root {
    --page-bg: #e6e6e6;
    --honey-light: #c29463;
    --honey-mid: #a9763f;
    --honey-deep: #8a5a2b;
    --honey-dark: #6e4520;
    --snow-tone: #d8b58c;
    --card-text: #ffffff;
    --card-shadow: rgba(0, 0, 0, 0.25);
  }

  * { margin: 0; padding: 0; box-sizing: border-box; }

  html, body {
    width: 1200px;
    height: 745px;
    overflow: hidden;
    background: var(--page-bg);
  }

  .stage {
    position: relative;
    width: 1200px;
    height: 745px;
    display: flex;
    align-items: center;
    justify-content: center;
  }

  .business-card {
    position: relative;
    width: 1040px;
    height: 594px;
    overflow: hidden;
    box-shadow: 0 10px 30px var(--card-shadow);
    color: var(--card-text);
    text-align: center;
  }

  .card-photo {
    position: absolute;
    inset: 0;
    background:
      radial-gradient(ellipse 42% 38% at 50% 34%, var(--snow-tone) 0%, rgba(216,181,140,0) 70%),
      linear-gradient(180deg,
        var(--honey-light) 0%,
        var(--honey-mid) 45%,
        var(--honey-deep) 72%,
        var(--honey-dark) 100%);
  }

  .card-content {
    position: relative;
    height: 100%;
    display: flex;
    flex-direction: column;
    align-items: center;
  }

  .brand-mark {
    margin-top: 110px;
    display: flex;
    align-items: center;
    gap: 14px;
    font-family: "Quicksand", sans-serif;
    font-weight: 300;
    font-size: 34px;
    line-height: 40px;
    letter-spacing: 6px;
    text-transform: uppercase;
  }

  .brand-mark__dot {
    width: 14px;
    height: 14px;
    border-radius: 50%;
    background: var(--card-text);
  }

  .brand-name {
    margin-top: 125px;
    font-family: "Dancing Script", cursive;
    font-weight: 700;
    font-size: 72px;
    line-height: 1;
  }

  .owner-name {
    margin-top: 18px;
    font-family: "Quicksand", sans-serif;
    font-weight: 300;
    font-size: 34px;
    line-height: 1.1;
  }

  .contact-list {
    margin-top: 16px;
    list-style: none;
    font-family: "Quicksand", sans-serif;
    font-weight: 400;
    font-size: 22px;
    line-height: 1;
  }

  .contact-list__item {
    display: flex;
    align-items: center;
    justify-content: center;
    gap: 6px;
    margin-bottom: 14px;
  }

  .contact-list__icon {
    width: 18px;
    height: 18px;
    fill: var(--card-text);
  }
</style>
</head>
<body>
  <main class="stage">
    <article class="business-card">
      <div class="card-photo" role="img" aria-label="Photograph of a snow-capped volcanic mountain rising above golden tussock plains, toned in warm honey amber"></div>

      <div class="card-content">
        <div class="brand-mark">
          <span class="brand-mark__dot"></span>
          <span>Pekeriu Honey</span>
        </div>

        <h1 class="brand-name">Pekeriu Honey</h1>
        <p class="owner-name">Manaia Brooks</p>

        <ul class="contact-list">
          <li class="contact-list__item">
            <svg class="contact-list__icon" viewBox="0 0 24 24" aria-hidden="true">
              <path d="M6.6 10.8a15.1 15.1 0 0 0 6.6 6.6l2.2-2.2c.3-.3.7-.4 1-.2 1.1.4 2.3.6 3.6.6.6 0 1 .4 1 1V20c0 .6-.4 1-1 1A17 17 0 0 1 3 4c0-.6.4-1 1-1h3.5c.6 0 1 .4 1 1 0 1.3.2 2.5.6 3.6.1.3 0 .7-.2 1z"/>
            </svg>
            <span>0217394461</span>
          </li>
          <li class="contact-list__item">
            <svg class="contact-list__icon" viewBox="0 0 24 24" aria-hidden="true">
              <path d="M3 5h18c.6 0 1 .4 1 1v12c0 .6-.4 1-1 1H3c-.6 0-1-.4-1-1V6c0-.6.4-1 1-1zm9 7.5L20 7H4z"/>
            </svg>
            <span>pekeriuhoney@tuimailbox.co.nz</span>
          </li>
        </ul>
      </div>
    </article>
  </main>
</body>
</html>
```